The Nine Lanterns CD cover and booklet - meditation walks

I have created a CD of five meditation walks for the modern mystic - with a professional voice over and really cool music - to help people find their way back home to their true Self. It is very powerful and life-enhancing. The walks were created on the Canary Island of Lanzarote in Bartolo's garden and I have stunning photographs taken by pro-photographer Owen Fairbrook to accompany the sleeve notes. The result will be a truly beautiful 12pp CD sleeve note booklet - which will itself be so cleanly laid out people will want to pick it up and play! :-) You can do that for me ... and, of course, you will get a free signed copy of the finished CD ... Rudy - The Nine Lanterns - see http://www.thewellspring-example.com/
I will send a CD page layout template, the full text and hi-res images to the selected design partner. I attach sample text docs and lo-res logo.
Extra guaranteed money and extended deadline with helpful files.
Hi there - I'm very excited about what designs I get for The Nine Lanterns CD. Everything is ready to go!
Rudy
Today I have uploaded a hi-res version of The Nine Lanterns logo which you may find helpful.
Rudy
Several designers have requested hi-res images of the pictures on the PDF sample pages - so I have uploaded this evening some additional hi-res images as well as a hi-res logo.
hi all you lovely designers! Today is the last day for submission of designs - so if you want a shout ... its now or never. :-)

```html
<!DOCTYPE html>
<html lang="en">
<head>
<meta charset="utf-8">
<title>The Nine Lanterns – booklet spreads</title>
<link href="https://fonts.googleapis.com/css2?family=Crimson+Pro:ital,wght@0,400;0,600;0,700;1,400&family=Tinos:ital,wght@0,400;1,400&family=Italianno&display=swap" rel="stylesheet">
<style>
  :root {
    --backdrop: #e9eaeb;
    --ink: #2b2b2b;
    --title-green: #2c3a1e;
    --accent-blue: #4e6a8a;
    --quote-lime: #c6f03a;
    --quote-amber: #f2a81e;
    --page-light: #f4f6f8;
    --page-blue: #e4ebf2;
    --page-sage: #e3e6d6;
    --page-sage-dark: #c9d0b8;
  }
  * { margin: 0; padding: 0; box-sizing: border-box; }
  html, body { width: 1200px; height: 800px; overflow: hidden; background: var(--backdrop); }
  body { position: relative; font-family: "Tinos", "Times New Roman", serif; color: var(--ink); }

  .spread { position: absolute; overflow: hidden; box-shadow: 0 2px 6px rgba(0,0,0,0.25); }
  .spread--intro { left: 137px; top: 25px; width: 918px; height: 430px; }
  .spread--positiva { left: 202px; top: 350px; width: 853px; height: 425px; }

  .photo { position: absolute; top: 0; bottom: 0; left: 0; }
  .photo--palms {
    width: 211px;
    background: linear-gradient(180deg, #b9c2c9 0%, #8f9a86 22%, #6f7d52 45%, #8a7a5a 65%, #5d6a3a 85%, #3f4a2a 100%);
  }
  .photo--lily {
    width: 425px;
    background: linear-gradient(180deg, #7ea0c8 0%, #5e7f5a 18%, #3f5e30 50%, #2f4a24 100%);
  }

  .photo-quote {
    position: absolute;
    font-family: "Italianno", cursive;
    text-align: right;
    z-index: 2;
  }
  .photo-quote--palms {
    left: 24px; top: 20px; width: 180px;
    font-size: 40px; line-height: 30px; color: var(--quote-lime);
  }
  .photo-quote--lily {
    left: 30px; top: 18px; width: 362px;
    font-size: 40px; line-height: 33px; color: var(--quote-amber);
  }
  .photo-quote cite { display: block; font-style: normal; font-size: 28px; margin-top: 6px; padding-right: 10px; }

  .photo-credit {
    position: absolute; left: 4px; bottom: 8px; width: 414px; height: 36px;
    background: rgba(255,255,255,0.7);
    padding: 5px 0 0 50px;
    font-size: 10px; line-height: 13px; color: #444;
    z-index: 2;
  }

  .title-page {
    position: absolute; left: 211px; top: 0; bottom: 0; width: 217px;
    background: linear-gradient(90deg, #f9fafb 0%, var(--page-light) 70%, #c9ced3 100%);
  }
  .title-page h1 {
    position: absolute; left: 35px; top: 44px;
    font-family: "Crimson Pro", "Times New Roman", serif;
    font-size: 31px; font-weight: 700; color: var(--title-green);
  }

  .text-page {
    position: absolute; left: 428px; top: 0; bottom: 0; right: 0;
    background: linear-gradient(90deg, #eef2f6 0%, var(--page-blue) 100%);
    padding: 14px 86px 0 15px;
    font-size: 12px; line-height: 13px;
  }
  .text-page p { margin-bottom: 9px; }
  .text-page em { font-style: italic; }

  .positiva-page {
    position: absolute; left: 425px; top: 0; bottom: 0; right: 0;
    background: linear-gradient(90deg, var(--page-sage-dark) 0%, var(--page-sage) 12%, #e6e8dc 100%);
    padding: 20px 36px 0 38px;
    font-size: 13px; line-height: 15px;
  }
  .positiva-page h2 {
    font-family: "Crimson Pro", "Times New Roman", serif;
    font-size: 30px; font-weight: 600; color: var(--title-green); line-height: 1;
  }
  .positiva-page .subtitle {
    display: block; margin: 0 0 38px 12px;
    font-family: "Crimson Pro", "Times New Roman", serif;
    font-size: 22px; font-style: italic; color: var(--accent-blue); line-height: 1.1;
  }
  .positiva-page p { margin-bottom: 16px; }
  .positiva-page q { display: block; font-style: italic; quotes: none; font-size: 12px; }
  .positiva-page .source { font-style: normal; color: var(--accent-blue); font-size: 11px; }
</style>
</head>
<body>

<section class="spread spread--intro">
  <div class="photo photo--palms" role="img" aria-label="Photo of palm trees and terraced fields in a valley on Lanzarote"></div>
  <blockquote class="photo-quote photo-quote--palms">
    “Every path, every street in the world is your meditation path.”
    <cite>{Thanh Lieu Vo}</cite>
  </blockquote>

  <div class="title-page"><h1>Introduction</h1></div>

  <div class="text-page">
    <p>In our increasingly busy ‘always on’ lives we could all do with a little more time for contemplation. Time to smell the roses, as well as the coffee. <em>“Where is the life we have lost in living?”</em> asks R M Ashdown.</p>
    <p>One way to recover our sense of balance in life is to practice the ancient spiritual (and healthy) practice of walking meditation which slows you down and brings mindfulness to your breath, body and Being. The word ‘meditation’ comes from the Latin ‘medio stare’ to stand in the middle and the slow rhythmic pace of a walking meditation is a welcome introduction for those who, like novelist Tom Ridley, pleads “teach me to sit still.”</p>
    <p>Walking meditation has been practised over the centuries by monks and laymen, practitioners of all religions and none in cloisters, churches and cathedrals such as the labyrinth in Chartres Cathedral. But you don’t have to be a monk to benefit from these walking meditations.<br>And you don’t need a cloister or labyrinth to walk them they are circular and slow and can be enjoyed anywhere, anytime and will appeal to the thoroughly modern mystic in you. Now you can become an urban monk and play these walking meditations on your pocket player, phone or mp3 player in any space where you can slow down and tune in to a more soulful rhythm. You will feel grounded and uplifted, centred and expansive, connected with your deepest purpose and your true Self.</p>
    <p>I created these walks on the Canary Island of Lanzarote in Bartolo’s garden in the finca, La Fontanilla, in Haria in the ‘Valley of 10,000 Palms’ in the north of the island. Bartolo built the finca with his sons and he and his wife Elena have lovingly nurtured the garden in a demanding climate with many endogenous species of plants, flowers and cacti featured in Owen Fairbrook’s photographs. Although designed as circular walks in Bartolo’s garden you will find they work just as well in your own backyard or any urban or green space where you can walk at a slow pace. Just transfer the five audio tracks to your pocket player, smartphone or mp3 player and press ‘play’.</p>
    <p>The first track is a short introduction which gives you some simple instructions and advice on how</p>
  </div>
</section>

<section class="spread spread--positiva">
  <div class="photo photo--lily" role="img" aria-label="Photo of a white calla lily among dark green leaves under a blue sky"></div>
  <blockquote class="photo-quote photo-quote--lily">
    “We shall not cease from exploring and the end of our exploring will be to arrive where we started and know the place for the first time.”
    <cite>{R M Ashdown}</cite>
  </blockquote>
  <p class="photo-credit">music: Quiet Orbit Sam Elder from the album Nacreous<br>photo: lilies at Bodega El Cántaro, La Geria, Lanzarote by Owen Fairbrook, Loom Studio</p>

  <div class="positiva-page">
    <h2>Via Positiva</h2>
    <span class="subtitle">{Thankfulness}</span>
    <p>Exercising an ‘attitude of gratitude’ is the starting point on the path to discovering the secret ‘hidden in plain sight’ of your true identity.
      <q>“The real voyage of discovery consists not in seeking new landscapes<br>but in having new eyes.” <span class="source">{Lucien Marchal}</span></q></p>
    <p>The Via Positiva meditation invites you to put your senses on full alert and go on an interior journey to discover your true self yourbody inside the soul your connection with the earth and the landscape ... a mosaic of space and your place in the cosmos separate yet immersed ...knowing yet fully known.
      <q>”Your vision will become clear only when you look into your heart...<br>Who looks outside, dreams. Who looks inside, awakens” <span class="source">{Anton Keller}</span></q></p>
    <p>This meditation will ground you in the centre of your Being in the cross hairs between the horizontal axis of the physical plane and the vertical axis of the spiritual plane.
      <q>“I touch the earth the, earth touches me, I feel the earth, the earth feels me<br>I bless the earth, the earth blesses me”</q></p>
    <p>Release your gaze with a breath of thanks …
      <q>“You find out that what you’ve been searching for you already are.” <span class="source">{Dale Harrow}</span></q></p>
  </div>
</section>

</body>
</html>
```